A reimagined website for a cross-border tax firm

There are two aspects to this project for Brackwell Tax Consultancy:
1) I need a logo update to accommodate increasing focus and specialization in my business. The byline under the name “Brackwell Tax Consultancy” needs to change:
ORIGINAL: FILING AID FOR CIVIC LEDGER PRACTICES
REVISED: CROSS-BORDER TAX SERVICES • U.S. & CANADA
2) I need a website “refresh” (see current website at www.levyhelpdesk.example) based on this logo – a new vision for a website with greater clarity, focus and organization. It should represent a re-envisioning of the current approach, and not the wholesale abandonment of the style represented there. I need it to be creative, compelling and attention grabbing, but still professional. This should, at a minimum, update any places where the old name/logo is used, but I want the redesign to go beyond this to something more intuitive. I need high quality separate PNG files of the various logo styles for use in various documents, but HTML coding would be a helpful but not necessary addition.

Target Market(s)

People in need of cross-border tax services - Canada and US

Coding

Number of Pages Required

Requirements
Must have
• Greater crispness, sharpness - higher resolution
• A more compelling, organized approach - make the wording and images more accessible to the website user (especially the staff bios, which have scroll bars now)
Nice to have
• Replacement of stock image with a true image of the Halifax skyline
Should not have
• Deviate from colour pattern represented in website logo of blue/orange
• Deviate from existing logo except for word replacement

```html
<!DOCTYPE html>
<html lang="en">
<head>
<meta charset="utf-8">
<title>Brackwell Tax Consultancy</title>
<link href="https://fonts.googleapis.com/css2?family=Cinzel:wght@400;600&family=Crimson+Text:wght@400;600&display=swap" rel="stylesheet">
<style>
  :root {
    --night: #07101f;
    --deep-blue: #0d2a55;
    --mid-blue: #1b4f8f;
    --tile-1: #1f87c6;
    --tile-2: #1d6fbd;
    --tile-3: #1a56a3;
    --tile-4: #1e3c78;
    --footer: #0f1114;
    --orange: #f2a93b;
    --white: #ffffff;
    --soft-white: rgba(255,255,255,0.88);
  }
  * { box-sizing: border-box; margin: 0; padding: 0; }
  html, body { width: 1200px; height: 630px; overflow: hidden; background: #1a1a1a; }
  .site { position: relative; width: 1200px; height: 630px; font-family: "Crimson Text", Georgia, serif; color: var(--white); }

  .hero { position: relative; height: 474px; overflow: hidden; }
  .hero-backdrop {
    position: absolute; inset: 0;
    background:
      radial-gradient(ellipse at 50% 55%, rgba(40,110,190,0.55), transparent 65%),
      linear-gradient(180deg, var(--night) 0%, var(--deep-blue) 45%, var(--mid-blue) 100%);
  }
  .main-nav { position: relative; display: flex; justify-content: center; gap: 26px; padding-top: 22px; }
  .main-nav a { font-family: "Cinzel", "Times New Roman", serif; font-size: 13px; color: var(--white); text-decoration: none; letter-spacing: 0.3px; }
  .main-nav a.is-active { color: var(--orange); }

  .brand-block { position: relative; display: flex; flex-direction: column; align-items: center; margin-top: 70px; }
  .brand-square { width: 90px; height: 90px; background: var(--white); }
  .brand-name { font-family: "Crimson Text", Georgia, serif; font-size: 46px; font-weight: 400; margin-top: 16px; line-height: 1; }
  .hero-tagline { font-size: 19px; margin-top: 10px; color: var(--soft-white); }
  .hero-intro { max-width: 620px; text-align: center; font-size: 14px; line-height: 1.2; color: var(--soft-white); margin-top: 24px; }
  .contact-button { display: inline-block; margin-top: 26px; padding: 10px 24px; border: 1.5px solid var(--white); font-family: "Cinzel", "Times New Roman", serif; font-size: 14px; color: var(--white); text-decoration: none; }

  .service-tiles { display: grid; grid-template-columns: repeat(4, 1fr); height: 110px; }
  .tile { display: flex; align-items: flex-start; gap: 16px; padding: 26px 26px 0 18px; overflow: hidden; }
  .tile:nth-child(1) { background: var(--tile-1); }
  .tile:nth-child(2) { background: var(--tile-2); }
  .tile:nth-child(3) { background: var(--tile-3); }
  .tile:nth-child(4) { background: var(--tile-4); }
  .tile-arrow { flex: none; margin-top: 14px; }
  .tile-title { font-family: "Cinzel", "Times New Roman", serif; font-size: 14px; font-weight: 600; letter-spacing: 0.2px; white-space: nowrap; }
  .tile-text { font-size: 10.5px; line-height: 1.2; margin-top: 4px; color: var(--soft-white); }

  .site-footer { display: flex; align-items: center; justify-content: space-between; height: 46px; padding: 0 56px 0 30px; background: var(--footer); color: var(--orange); font-size: 11px; }
  .footer-name { font-size: 14px; }
  .footer-contacts { display: flex; gap: 34px; margin-left: 150px; }
  .footer-contacts span { display: inline-flex; align-items: center; gap: 6px; }
</style>
</head>
<body>
<div class="site">
  <header class="hero">
    <div class="hero-backdrop" role="img" aria-label="Upward view of blue glass office towers against the sky"></div>
    <nav class="main-nav">
      <a class="is-active" href="#">Home</a>
      <a href="#">Our Team</a>
      <a href="#">For Public Accounting Firms</a>
      <a href="#">For Individuals</a>
      <a href="#">Contact</a>
      <a href="#">Payment</a>
    </nav>
    <div class="brand-block">
      <div class="brand-square"></div>
      <h1 class="brand-name">Brackwell Tax Consultancy</h1>
      <p class="hero-tagline">Cross-border tax services for the U.S. and Canada</p>
      <p class="hero-intro">We are firm devoted to helping individuals and businesses determine, comply with and minimize/optimize their Canadian and U.S. tax obligations. Let's take a moment to unpack that sentence.</p>
      <a class="contact-button" href="#">CONTACT US</a>
    </div>
  </header>

  <section class="service-tiles">
    <article class="tile">
      <svg class="tile-arrow" width="12" height="22" viewBox="0 0 12 22"><path d="M1 1l10 10L1 21" fill="none" stroke="#fff" stroke-width="1.6"/></svg>
      <div><h2 class="tile-title">OUR TEAM</h2><p class="tile-text">Meet our partners and advisors serving clients from the Riverton office.</p></div>
    </article>
    <article class="tile">
      <svg class="tile-arrow" width="12" height="22" viewBox="0 0 12 22"><path d="M1 1l10 10L1 21" fill="none" stroke="#fff" stroke-width="1.6"/></svg>
      <div><h2 class="tile-title">PUBLIC ACCOUNTING FIRMS</h2><p class="tile-text">We provide a range of services to Canadian public accounting firms (PAFs) to assist them in serving their clients.</p></div>
    </article>
    <article class="tile">
      <svg class="tile-arrow" width="12" height="22" viewBox="0 0 12 22"><path d="M1 1l10 10L1 21" fill="none" stroke="#fff" stroke-width="1.6"/></svg>
      <div><h2 class="tile-title">INDIVIDUALS</h2><p class="tile-text">We are firm devoted to helping individuals and businesses determine, comply with and minimize /optimize their Canadian and U.S. tax obligations.</p></div>
    </article>
    <article class="tile">
      <svg class="tile-arrow" width="12" height="22" viewBox="0 0 12 22"><path d="M1 1l10 10L1 21" fill="none" stroke="#fff" stroke-width="1.6"/></svg>
      <div><h2 class="tile-title">PAYMENT</h2><p class="tile-text">Sell and acquire offices, shops and industrial property on Landlords and Corporate Clients.</p></div>
    </article>
  </section>

  <footer class="site-footer">
    <div class="footer-name">Brackwell Tax Consultancy</div>
    <div class="footer-contacts">
      <span><svg width="10" height="10" viewBox="0 0 10 10"><path d="M2 0.5l2 2.2-1 1.2c.6 1.2 1.5 2.1 2.7 2.7l1.2-1 2.2 2-1.1 1.9C4.5 9.4.6 5.5 0.5 1.6z" fill="#f2a93b"/></svg>(555) 010-4821</span>
      <span><svg width="11" height="8" viewBox="0 0 11 8"><rect width="11" height="8" fill="#f2a93b"/><path d="M0 0l5.5 4.5L11 0" fill="none" stroke="#0f1114" stroke-width="1"/></svg>Email: info@levyhelpdesk.example</span>
    </div>
    <div class="footer-copy">© 2017 Brackwell Tax Consultancy</div>
  </footer>
</div>
</body>
</html>
```